Business cards for Wine company
Caspellini
Project: Business cards for Wine company
Business cards for Wine company - Beverages
Creative Brief
Simple
Taco Vermeulen
Managing Director
Lindeboomlaan 23 6191KM BEEKDAL
info@caspellini.example
www.caspellini.example
Would be nice if there is a facebook and a twitter in there... twitter @caspellini facebook/caspellini
Be creative!

```html
<!DOCTYPE html>
<html lang="en">
<head>
<meta charset="utf-8">
<title>Caspellini – Business Cards</title>
<link rel="stylesheet" href="https://fonts.googleapis.com/css2?family=Libre+Baskerville:wght@400;700&display=swap">
<style>
  :root {
    --stage: #e4e4e4;
    --card-white: #ffffff;
    --card-fade: #ececec;
    --card-black: #1c1c1c;
    --card-black-edge: #0b0b0b;
    --ink: #2b2b2b;
    --ink-soft: #555555;
    --accent: #b3262a;
    --ornament-light: #e2e2e2;
    --ornament-dark: #2b2b2b;
    --back-text: #5c5c5c;
  }
  * { margin: 0; padding: 0; box-sizing: border-box; }
  html, body {
    width: 1200px; height: 871px; overflow: hidden;
    background: var(--stage);
    font-family: "Libre Baskerville", Georgia, serif;
    color: var(--ink);
  }
  .stage {
    position: relative; width: 1200px; height: 871px;
    display: flex; flex-direction: column; align-items: center;
    justify-content: center; gap: 30px;
  }
  .card {
    position: relative; width: 680px; height: 388px;
    border-radius: 22px; overflow: hidden;
    box-shadow: 0 6px 18px rgba(0,0,0,0.18);
  }

  /* Back side */
  .card-back {
    background: radial-gradient(ellipse at 30% 30%, var(--card-black) 0%, var(--card-black-edge) 100%);
  }
  .card-back .vine {
    position: absolute; left: 40px; top: 30px; width: 300px; height: 330px;
    border-radius: 50%;
    background: radial-gradient(ellipse at 40% 45%, var(--ornament-dark) 0%, rgba(43,43,43,0) 70%);
  }
  .card-back .web {
    position: absolute; left: 330px; top: 70px;
    font-size: 15px; letter-spacing: 3px; color: var(--back-text);
  }

  /* Front side */
  .card-front {
    background: linear-gradient(115deg, var(--card-white) 45%, var(--card-fade) 100%);
  }
  .card-front .vine {
    position: absolute; right: 30px; top: 120px; width: 300px; height: 220px;
    border-radius: 50%;
    background: radial-gradient(ellipse at 50% 50%, var(--ornament-light) 0%, rgba(226,226,226,0) 70%);
  }
  .brand {
    position: absolute; left: 42px; top: 34px; width: 300px; text-align: center;
  }
  .brand-name {
    font-size: 40px; font-weight: 400; letter-spacing: 1px; color: var(--ink);
    line-height: 1;
  }
  .brand-dot {
    display: block; width: 34px; height: 34px; border-radius: 50%;
    background: var(--accent); margin: 12px auto 8px;
  }
  .brand-est {
    font-size: 15px; letter-spacing: 2px; color: var(--ink);
  }
  .contact {
    position: absolute; left: 42px; top: 212px; font-size: 13px; color: var(--ink);
  }
  .contact-row { display: flex; align-items: center; gap: 8px; height: 22px; }
  .contact-row .sep { color: var(--ink-soft); margin: 0 4px; }
  .address { display: flex; gap: 8px; margin-bottom: 8px; line-height: 20px; }
  .icon {
    display: inline-flex; width: 14px; height: 12px; flex: none;
    background: var(--accent); border-radius: 2px;
    align-items: center; justify-content: center;
  }
  .icon svg { width: 10px; height: 10px; }
  .icon-pin { background: none; height: 14px; }
  .icon-pin svg { width: 12px; height: 14px; }
  .person {
    position: absolute; left: 470px; top: 300px;
  }
  .person-name { font-size: 19px; color: var(--accent); }
  .person-role { font-size: 14px; color: var(--ink-soft); margin-top: 3px; }
</style>
</head>
<body>
<main class="stage">
  <section class="card card-back" aria-label="Card back">
    <div class="vine" role="img" aria-label="Faint grape vine ornament"></div>
    <p class="web">www.caspellini.example</p>
  </section>

  <section class="card card-front" aria-label="Card front">
    <div class="vine" role="img" aria-label="Faint grape leaf and vine ornament"></div>

    <div class="brand">
      <p class="brand-name">CASPELLINI</p>
      <span class="brand-dot"></span>
      <p class="brand-est">EST 2012</p>
    </div>

    <div class="contact">
      <div class="address">
        <span class="icon icon-pin">
          <svg viewBox="0 0 12 14"><path d="M6 0a5 5 0 0 0-5 5c0 4 5 9 5 9s5-5 5-9a5 5 0 0 0-5-5z" fill="#b3262a"/><circle cx="6" cy="5" r="2" fill="#fff"/></svg>
        </span>
        <p>Lindeboomlaan 23<br>6191KM BEEKDAL</p>
      </div>
      <div class="contact-row">
        <span class="icon"><svg viewBox="0 0 10 10"><path d="M2 1h2l1 2-1 1a5 5 0 0 0 2 2l1-1 2 1v2c-4 0-7-3-7-7z" fill="#fff"/></svg></span>
        <span>+ 00 000 0000</span><span class="sep">|</span>
        <span class="icon"><svg viewBox="0 0 10 10"><rect x="3" y="1" width="4" height="8" rx="1" fill="#fff"/></svg></span>
        <span>+ 31 612345678</span>
      </div>
      <div class="contact-row">
        <span class="icon"><svg viewBox="0 0 10 10"><rect x="1" y="2" width="8" height="6" fill="#fff"/><path d="M1 2l4 3 4-3" stroke="#b3262a" fill="none"/></svg></span>
        <span>info@caspellini.example</span><span class="sep">|</span>
        <span class="icon"><svg viewBox="0 0 10 10"><circle cx="5" cy="5" r="3.5" stroke="#fff" fill="none"/></svg></span>
        <span>www.caspellini.example</span>
      </div>
      <div class="contact-row">
        <span class="icon"></span>
        <span>@caspellini</span><span class="sep">|</span>
        <span class="icon"></span>
        <span>@caspellini</span>
      </div>
    </div>

    <div class="person">
      <p class="person-name">Taco Vermeulen</p>
      <p class="person-role">Managing Director</p>
    </div>
  </section>
</main>
</body>
</html>
```